Letterhead Design

I have my company logo, slogan, etc. please refer to attachment for your onward design.

An Overview / Background of the Business & Services – Specialised in high-end boutique interior furnishing and fabricate furniture.

The Target Market / Audience you are trying to reach – Global client to US for high-end brand. 90% of our client are from USA.

Design Specifics; any preferences or ideas for Style, Colour, Imagery, etc – No. We have our own logo and slogan, hence would need design of letterhead, business card, envelopes and complimentary slip, if possible, otherwise letterhead will do.

Industry/Entity Type

Boutique

```html
<!DOCTYPE html>
<html lang="en">
<head>
<meta charset="utf-8">
<title>Northvale Interior – Letterhead</title>
<link rel="stylesheet" href="https://fonts.googleapis.com/css2?family=Jost:wght@400;500;600&display=swap">
<style>
  :root {
    --paper: #ffffff;
    --band: #f4e4d6;
    --band-deep: #ecd6c4;
    --ink: #4a2a20;
    --ink-soft: #6b4a3e;
  }
  html, body {
    margin: 0;
    padding: 0;
    overflow: hidden;
    background: var(--paper);
  }
  .letterhead {
    position: relative;
    width: 852px;
    height: 1200px;
    overflow: hidden;
    background: var(--paper);
    font-family: "Jost", "Century Gothic", sans-serif;
    color: var(--ink);
  }
  .header-band {
    position: absolute;
    left: 0; top: 0;
    width: 852px;
    height: 217px;
    background: linear-gradient(100deg, var(--band) 0%, var(--band-deep) 50%, var(--band) 100%);
  }
  .footer-band {
    position: absolute;
    left: 0; top: 1103px;
    width: 852px;
    height: 97px;
    background: linear-gradient(100deg, var(--band-deep) 0%, var(--band) 50%, var(--band-deep) 100%);
  }
  .brand-name {
    position: absolute;
    left: 333px; top: 30px;
    width: 197px;
    height: 148px;
    display: flex;
    flex-direction: column;
    align-items: center;
    justify-content: center;
    margin: 0;
    font-size: 34px;
    font-weight: 500;
    line-height: 1.05;
    letter-spacing: 1px;
    text-transform: uppercase;
    color: var(--ink);
    text-align: center;
  }
  .registration {
    position: absolute;
    left: 340px; top: 190px;
    margin: 0;
    font-size: 9.5px;
    letter-spacing: 1px;
    color: var(--ink-soft);
  }
  .contact {
    position: absolute;
    left: 240px; top: 1121px;
    width: 474px;
    margin: 0;
    text-align: center;
    font-size: 13px;
    line-height: 18px;
    font-style: normal;
    letter-spacing: 0.5px;
    color: var(--ink);
  }
  .contact strong { font-weight: 600; }
  .footer-mark {
    position: absolute;
    left: 756px; top: 1124px;
    width: 68px;
    height: 46px;
    display: flex;
    flex-direction: column;
    align-items: center;
    justify-content: center;
    font-size: 10px;
    font-weight: 500;
    line-height: 1.1;
    text-transform: uppercase;
    color: var(--ink);
    text-align: center;
  }
</style>
</head>
<body>
  <main class="letterhead">
    <header>
      <div class="header-band" role="img" aria-label="Faint architectural sketch of building lines in soft beige"></div>
      <h1 class="brand-name"><span>Northvale</span><span>Interior</span></h1>
      <p class="registration">UEN/GST : 201904172M</p>
    </header>

    <footer>
      <div class="footer-band" role="img" aria-label="Faint architectural sketch of building lines in soft beige"></div>
      <address class="contact">
        <strong>Address Line</strong><br>
        <strong>Tel:</strong> 00 00 0000 0000 <strong>Fax:</strong> 00 0000 0000<br>
        <strong>Email:</strong> abc@def <strong>www.abcdef.com</strong>
      </address>
      <div class="footer-mark"><span>Northvale</span><span>Interior</span></div>
    </footer>
  </main>
</body>
</html>
```